MLOrchard
Home Page
MLOrchard -
Creative Brief
maplethornorchard.example
This company is comprised of two things: 1) a produce market that sells a variety of berries and 2) a strawberry farm where you can pick your own and participate in a variety of activities for the family.
Likes www.brookvalegroves.example. Likes the pictures of families and children having fun. Site should present a fun environment.
Friendly
For Children
Fun
Red for strawberries
Green for strawberries
Yellow to go with logo
below header
www.brookvalegroves.example
There needs to be a horizontal slideshow on the home page. The slideshow should span the width of the site. There should be a top horizontal banner with the main navigation bar running horizontally under the banner and then the slideshow should be under the main horizontal navigation. Site should be approximately 1,050 pixels wide and about 750-850 pixels long. The main navigation bar should contain the following links: Home, Our History, Berry Farm, Berry Market, Map/Directions/Contact, Coupons/Specials, Sign up for Specials

```html
<!DOCTYPE html>
<html lang="en">
<head>
<meta charset="utf-8">
<title>Maplethorn Orchard – Home</title>
<link rel="stylesheet" href="https://fonts.googleapis.com/css2?family=PT+Sans:wght@400;700&display=swap">
<style>
  :root {
    --green-dark: #0d4a12;
    --green: #2f8a26;
    --green-bright: #5fc23a;
    --green-button: #1f6b2a;
    --red: #d93a25;
    --red-dark: #8a1a10;
    --red-tab: #e04a2e;
    --yellow: #ffe033;
    --white: #ffffff;
    --text: #222222;
    --panel-border: #e8e8e8;
  }
  * { box-sizing: border-box; margin: 0; padding: 0; }
  html, body { width: 1200px; height: 925px; overflow: hidden; }
  body { position: relative; font-family: "PT Sans", sans-serif; color: var(--text); }

  .backdrop {
    position: absolute; inset: 0;
    background:
      linear-gradient(180deg, var(--green-dark) 0%, #1f7a1c 8%, var(--green-bright) 15%, #2b6e1f 22%, rgba(0,0,0,0) 32%),
      radial-gradient(ellipse at 10% 60%, #c8271a 0%, #8e140c 35%, rgba(0,0,0,0) 60%),
      radial-gradient(ellipse at 92% 55%, #d0301e 0%, #7a120a 35%, rgba(0,0,0,0) 60%),
      linear-gradient(180deg, #2a5a1a 30%, #6b1a10 70%, #3a0c08 100%);
  }

  .brand { position: absolute; left: 160px; top: 40px; display: flex; align-items: center; gap: 14px; }
  .brand-mark { width: 60px; height: 60px; border-radius: 50%; background: var(--red); }
  .brand-name { font-size: 30px; font-weight: 700; color: var(--white); white-space: nowrap; }

  .phone { position: absolute; left: 775px; top: 104px; display: flex; align-items: center; gap: 12px; color: var(--white); font-size: 22px; white-space: nowrap; }
  .berry-art { position: absolute; left: 960px; top: 92px; width: 90px; height: 53px; border-radius: 40px 40px 10px 10px; background: radial-gradient(circle at 50% 70%, #e0321f, #9c1a0e); }

  .main-nav { position: absolute; left: 137px; top: 145px; width: 926px; height: 48px; display: flex; background: var(--red-tab); }
  .main-nav a { flex: 1 1 auto; display: flex; align-items: center; justify-content: center; color: var(--white); text-decoration: none; font-size: 20px; border-left: 2px solid #b83220; white-space: nowrap; }
  .main-nav a:first-child { border-left: 0; }
  .main-nav a.is-current { flex: 0 0 84px; background: var(--green); }

  .content { position: absolute; left: 137px; top: 220px; width: 926px; height: 450px; background: var(--white); }

  .slideshow { position: absolute; left: 18px; top: 17px; width: 890px; height: 301px; background: linear-gradient(90deg, #163f1a 0%, #2f6a2a 40%, #b9d1a5 60%, #eef3e4 100%); overflow: hidden; }
  .slide-photo { position: absolute; right: 60px; top: 40px; width: 300px; height: 210px; border-radius: 50%; background: radial-gradient(circle at 50% 45%, #f04a30, #b81d10 70%, rgba(0,0,0,0) 72%); }
  .slide-copy { position: absolute; left: 45px; top: 50px; width: 360px; color: var(--white); font-size: 16px; line-height: 1.35; }
  .slide-title { color: var(--yellow); font-size: 27px; font-weight: 700; line-height: 1.2; margin-bottom: 8px; white-space: nowrap; }
  .slide-copy p + p { margin-top: 20px; }
  .btn { display: inline-flex; align-items: center; justify-content: center; background: var(--green-button); color: var(--white); font-size: 15px; border-radius: 3px; white-space: nowrap; }
  .slide-more { position: absolute; left: 165px; top: 258px; width: 100px; height: 22px; }
  .slide-dots { position: absolute; right: 40px; bottom: 12px; display: flex; gap: 4px; }
  .slide-dots span { width: 8px; height: 8px; border-radius: 50%; background: var(--red); }

  .teaser { position: absolute; top: 330px; width: 290px; height: 105px; border: 1px solid var(--panel-border); background: linear-gradient(90deg, rgba(255,255,255,0.95) 55%, rgba(255,255,255,0.5)), linear-gradient(180deg, #f3c9bc, #c8352a); padding: 6px 10px; }
  .teaser h2 { color: var(--red); font-size: 19px; font-weight: 700; line-height: 1.1; }
  .teaser p { font-size: 14px; line-height: 1.1; width: 230px; }
  .teaser .btn { position: absolute; right: 12px; bottom: 8px; width: 60px; height: 18px; font-size: 12px; }
  .teaser--info { left: 18px; }
  .teaser--market { left: 318px; }
  .teaser--news { left: 618px; background: #f6f6f6; }
  .news-input { margin-top: 8px; width: 265px; height: 22px; border: 1px solid #bbb; background: var(--white); font-size: 12px; padding: 3px 6px; color: #555; }
  .teaser--news .btn { width: 70px; }

  .welcome { position: absolute; left: 137px; top: 690px; width: 926px; height: 160px; background: var(--white); }
  .welcome h1 { position: absolute; left: 25px; top: 15px; color: var(--green); font-size: 20px; font-weight: 400; }
  .welcome p { position: absolute; left: 60px; top: 45px; width: 620px; text-align: center; font-size: 12.5px; line-height: 1.35; }
  .bowl-art { position: absolute; left: 665px; top: 15px; width: 225px; height: 132px; border-radius: 50%; background: radial-gradient(circle at 50% 55%, #d7302a 0%, #f2d9d6 45%, #ffffff 70%); }

  .social { position: absolute; left: 158px; top: 860px; display: flex; gap: 18px; }
  .social span { width: 38px; height: 38px; border-radius: 50%; background: #3a6bb0; }
  .social span + span { background: #48a6dd; }
  .copyright { position: absolute; left: 675px; top: 868px; width: 383px; height: 28px; background: var(--red-dark); color: var(--white); font-size: 13px; display: flex; align-items: center; padding-left: 12px; }
</style>
</head>
<body>
  <div class="backdrop" role="img" aria-label="Close-up photo of ripe strawberries among green leaves"></div>

  <header>
    <div class="brand"><span class="brand-mark"></span><span class="brand-name">Maplethorn Orchard</span></div>
    <div class="phone">
      <svg width="30" height="23" viewBox="0 0 34 26" aria-hidden="true"><path d="M3 8c0-4 28-4 28 0v3h-7V8H10v3H3z" fill="#fff"/><rect x="7" y="13" width="20" height="11" rx="2" fill="#fff"/><circle cx="17" cy="18.5" r="3" fill="#1f5c1a"/></svg>
      <span>000-0000-000</span>
    </div>
    <div class="berry-art" role="img" aria-label="Strawberry illustration"></div>
  </header>

  <nav class="main-nav">
    <a href="#" class="is-current">Home</a>
    <a href="#">Farm info</a>
    <a href="#">About</a>
    <a href="#">Farm market</a>
    <a href="#">School tours</a>
    <a href="#">Get a map</a>
    <a href="#">Calender</a>
    <a href="#">Contact Us</a>
  </nav>

  <main class="content">
    <section class="slideshow">
      <div class="slide-photo" role="img" aria-label="Photo of a heart-shaped strawberry"></div>
      <div class="slide-copy">
        <div class="slide-title">Lorem ipsum dolor sit amet</div>
        <p>Sed egestas in auctor, ut! Facilisis, elementum dapibus, magnis augue! Tortor massa scelerisque montes cursus.</p>
        <p>Turpis cras magna urna! Et a nisi mid, porttitor! Proin enim odio, ut tincidunt! Dolor sagittis habitasse</p>
      </div>
      <a class="btn slide-more">Read More</a>
      <div class="slide-dots"><span></span><span></span><span></span><span></span></div>
    </section>

    <section class="teaser teaser--info">
      <h2>Farm info</h2>
      <p>Ut, tristique tincidunt penatibus purus mauris vel a odio ridiculus urna</p>
      <a class="btn">More</a>
    </section>
    <section class="teaser teaser--market">
      <h2>Farm market</h2>
      <p>Ut, tristique tincidunt penatibus purus mauris vel a odio ridiculus urna</p>
      <a class="btn">More</a>
    </section>
    <section class="teaser teaser--news">
      <h2>Join News Letter</h2>
      <div class="news-input">Email Address...</div>
      <a class="btn">Send</a>
    </section>
  </main>

  <section class="welcome">
    <h1>Welcome To Maplethorn Orchard</h1>
    <p>Massa porttitor pid vut egestas! Lacus et odio pulvinar cursus parturient, lacus dictumst integer? Lacus massa eros lacus, lorem adipiscing rhoncus in massa mid porttitor magnis urna? Elit penatibus nec porttitor porta, non massa mauris augue parturient magna pellentesque ultrices pellentesque pid dignissim integer! Integer porttitor penatibus scelerisque nec massa, et odio hac penatibus eros augue pid sed porttitor, lectus et nec elementum adipiscing turpis arcu, mid sociis in scelerisque tincidunt elit placerat ultricies arcu! Tincidunt elementum montes elit.</p>
    <div class="bowl-art" role="img" aria-label="Photo of a bowl of strawberries"></div>
  </section>

  <footer>
    <div class="social"><span aria-label="Social link"></span><span aria-label="Social link"></span></div>
    <div class="copyright">Copyright (c) 2011 All Rights Reserved</div>
  </footer>
</body>
</html>
```